Photo Montage company looking for fun AND informative ad slick

Looking for fun AND informative ad that can be used as the front of an ad slick(Example in uploaded files). That is US letter, 215.9 by 279.4 mm. Items not fitting that size are immediately excluded. The company "Brightwell Frames" , logo is included as .ai file. What we do is provide a device that you hook to a TV (6 example pics given. Only the "sandr*" or "granny*" can be used due to copyright issues. {The ones with the fat ugly guy and beautiful Guyanese Indian woman, since thats us} If you want to use Pixelgrove images I will pay directly for them once your design is selected, mock up can contain their watermark and MUST include their inventory # for even consideration. Any photo that isn't our logo or starts with sandr is NOT licensed by us and CAN NOT be used. Pictures we didn't provide that DO NOT have the related Pixelgrove inventory number WILL NOT BE CONSIDERED. Copyright violations are NOT what we are about) that shows a photo montage. But not like any normal same pictures in the same sequence. With ours, you can have a website where before the event (Wedding, retirement party, birthday party, etc) people can upload pictures. Then, at the event, they can email and text pictures they take there and they'll add to the screen. Finally, an optional camera on the tv will take pictures and add them into the mix. Finally, it randomly displays all the pics so its not the same sequence all the time. We want to emphasize that this isn't a normal old type of montage that doesn't change and is in the same order, that its interactive. We want to stress that you can add pictures during the event by text and email. Maybe say something that we don't lock you into packages, it all can be customized. Our website is http://brightwell.frames/ (Yes, its a .pictures domain), email is hello@brightwell.frames, phone is 1-844-GO-TULKS and our address is PO Box 47, Dunmore, NY 12644. We are ready to move fast, so expect replies quickly!
Updates

Target Market(s)

Weddings, Birthdays, any party

Industry/Entity Type

Technical Service

Number of Pages Required

2 page

Requirements
Must have
• Important to stress this isn't a typical photo montage. Interactive additions via text, email, and camera mounted on TV at party.
Should not have
• Images that are NOT licensed or include photos that DO NOT have a Pixelgrove inventory number on submission

```html
<!DOCTYPE html>
<html lang="en">
<head>
<meta charset="utf-8">
<title>Brightwell Frames – Get Your Picture on the Screen</title>
<link href="https://fonts.googleapis.com/css2?family=Yanone+Kaffeesatz:wght@300;400;500&display=swap" rel="stylesheet">
<style>
  :root {
    --page-bg: #ecebe8;
    --cream: #fbf8ea;
    --ink: #1c1c1c;
    --rose: #d9616b;
    --pattern-green: #6cc08e;
    --pattern-mint: #8fd3a8;
    --pattern-salmon: #eb8c82;
    --pattern-yellow: #efe07e;
    --photo-dark: #3b3a38;
    --photo-grey: #a9a8a4;
  }
  * { margin: 0; padding: 0; box-sizing: border-box; }
  html, body { width: 899px; height: 1200px; overflow: hidden; }
  body {
    background: var(--page-bg);
    font-family: "Yanone Kaffeesatz", "Arial Narrow", sans-serif;
    color: var(--ink);
    position: relative;
  }

  /* US letter page: 215.9 × 279.4 mm → 880 × 1140 px */
  .letter-page {
    position: absolute;
    left: 9px; top: 30px;
    width: 880px; height: 1140px;
    overflow: hidden;
    box-shadow: 0 6px 18px rgba(0,0,0,.18);
  }
  .pattern-band {
    position: absolute; inset: 0;
    background: linear-gradient(160deg, var(--pattern-green) 0%, var(--pattern-yellow) 35%, var(--pattern-salmon) 60%, var(--pattern-mint) 100%);
  }
  .panel {
    position: absolute;
    left: 60px; right: 60px;
    background: var(--cream);
    box-shadow: 0 2px 6px rgba(0,0,0,.2);
  }
  .panel--main { top: 60px; height: 760px; }
  .panel--contact { top: 880px; height: 200px; }

  .headline {
    text-align: center;
    margin-top: 48px;
    font-weight: 300;
    line-height: 1;
    letter-spacing: 3px;
  }
  .headline__top { display: block; font-size: 86px; color: var(--ink); text-shadow: 1px 2px 2px rgba(0,0,0,.25); }
  .headline__bottom { display: block; font-size: 86px; color: var(--rose); margin-top: 18px; text-shadow: 1px 2px 2px rgba(0,0,0,.2); }

  .product-photo {
    position: absolute;
    left: 30px; top: 290px;
    width: 310px; height: 400px;
    background: linear-gradient(180deg, var(--photo-dark) 0%, var(--photo-dark) 28%, var(--photo-grey) 45%, #c8c7c2 80%, #6d5a48 100%);
    border: 1px solid #b9b9b9;
    box-shadow: 3px 4px 8px rgba(0,0,0,.35);
  }

  .feature-list {
    position: absolute;
    left: 360px; right: 20px; top: 310px;
    list-style: none;
    text-align: center;
  }
  .feature { margin-bottom: 16px; }
  .feature__title { display: block; font-size: 38px; color: var(--rose); line-height: 1; font-weight: 300; }
  .feature__note { display: block; font-size: 19px; color: var(--ink); line-height: 1.15; font-weight: 300; }
  .feature--closing .feature__title { line-height: 1.1; }

  .custom-note {
    position: absolute;
    left: 20px; right: 20px; top: 710px;
    text-align: center;
    font-size: 26px;
    font-weight: 400;
    line-height: 1;
    color: var(--ink);
  }
  .custom-note em { font-style: normal; color: var(--rose); }

  .contact-list {
    position: absolute;
    left: 36px; top: 42px;
    list-style: none;
    font-size: 23px;
    line-height: 1.3;
    font-weight: 300;
  }
  .contact-list .label { color: var(--rose); }

  .brand {
    position: absolute;
    right: 50px; top: 46px;
    display: flex; flex-direction: column; align-items: center;
  }
  .brand__mark { width: 54px; height: 54px; background: var(--rose); margin-bottom: 10px; }
  .brand__name { font-size: 36px; font-weight: 400; color: var(--ink); line-height: 1; }
</style>
</head>
<body>
  <main class="letter-page">
    <div class="pattern-band" role="img" aria-label="Colourful geometric diamond pattern in green, salmon and yellow"></div>

    <section class="panel panel--main">
      <h1 class="headline">
        <span class="headline__top">GET YOUR PICTURE</span>
        <span class="headline__bottom">ON THE SCREEN!</span>
      </h1>

      <div class="product-photo" role="img" aria-label="Photo of a wedding slideshow shown on a TV mounted on a metal stand"></div>

      <ul class="feature-list">
        <li class="feature">
          <span class="feature__title">Upload pictures</span>
          <span class="feature__note">on our website before or during the event</span>
        </li>
        <li class="feature">
          <span class="feature__title">E-mail or text</span>
          <span class="feature__note">pictures on the spot</span>
        </li>
        <li class="feature">
          <span class="feature__title">Take pictures</span>
          <span class="feature__note">on the spot with the built in camera</span>
        </li>
        <li class="feature feature--closing">
          <span class="feature__title">Have your pictures<br>interactively show up<br>on the screen!</span>
        </li>
      </ul>

      <p class="custom-note">No locked packages – <em>everything can be customized!</em></p>
    </section>

    <section class="panel panel--contact">
      <ul class="contact-list">
        <li><span class="label">web:</span> http://brightwell.frames/</li>
        <li><span class="label">e-mail:</span> hello@brightwell.frames</li>
        <li><span class="label">phone:</span> 1-844-GO-TULKS</li>
        <li><span class="label">address:</span> PO Box 47, Dunmore, NY 12644</li>
      </ul>
      <div class="brand">
        <span class="brand__mark"></span>
        <span class="brand__name">brightwellframes</span>
      </div>
    </section>
  </main>
</body>
</html>
```